Logo & Visitenkarte für Elterncoaching, Einzel,- Paar- und Familientherapie
Tolle eigene kreative Umsetzung, super schnell in der Kommunikation und im Umgang mit Input. Eine große Unterstützung und sehr professionell. Die Zusammenarbeit hat viel Spaß gemacht und ich kann Nachtfalke empfehlen!
Zielgruppe
Tätigkeit: Elterncoaching, Einzel,- Paar- und Familientherapie
Zielgruppe: Eltern kleiner Kinder, Paare, Einzelne Personen die nicht mehr weiter wissen oder einfach eine neue Idee / Perspektiven benötigen
Aufgabenstellung
Auf die Visitenkarte soll ein Logo bzw. eine Grafik dargestellt werden, welche ebenfalls auf der Website und dem Flyer genutzt werden soll wird es hier als Logo bezeichnet.
Die Grafik soll ein Labyrinth und eine Person in einer scheinbar aussichtsloser Lage darstellen mit der Frage „ANKER gefällig?“ (siehe Idee im Datenanhang).
Die Figur soll oben links stehen und in Richtung Labyrinth blicken (hier zu beachten dass es bei einem eventuellen Druck von Visitenkarten mit abgerundeten Kanten nicht angeschnitten wird).
WICHTIG: bei der Figur soll nicht zu erkennen sein ob es sich um eine weibliche oder männliche Person handelt, es soll sowohl für Einzelpersonen als auch für Paare oder Familien ansprechend wirken.

```html
<!DOCTYPE html>
<html lang="de">
<head>
<meta charset="utf-8">
<title>Lichtung Praxis – Visitenkarte</title>
<link rel="stylesheet" href="https://fonts.googleapis.com/css2?family=Barlow+Semi+Condensed:wght@300;500;600&family=Open+Sans:wght@400;600&display=swap">
<style>
  :root {
    --backdrop: #e6e7e8;
    --teal: #00b5c0;
    --paper: #ffffff;
    --ink: #1a1a1a;
    --reverse: #ffffff;
    --shadow: rgba(0, 0, 0, 0.18);
  }
  * { box-sizing: border-box; margin: 0; padding: 0; }
  html, body {
    width: 1200px;
    height: 895px;
    overflow: hidden;
    background: var(--backdrop);
  }
  .sheet {
    position: relative;
    width: 1200px;
    height: 895px;
    display: flex;
    justify-content: center;
    align-items: center;
    gap: 80px;
  }
  .card {
    width: 440px;
    height: 680px;
    position: relative;
    box-shadow: 0 10px 30px var(--shadow);
  }

  /* Front side */
  .card--front { background: var(--teal); color: var(--reverse); }
  .front-lockup {
    position: absolute;
    left: 50%;
    top: 50%;
    transform: translate(-50%, -50%) rotate(-90deg);
    display: flex;
    align-items: center;
    gap: 26px;
    white-space: nowrap;
  }
  .front-lockup__dot {
    width: 110px;
    height: 110px;
    border-radius: 50%;
    border: 6px solid var(--reverse);
    flex: none;
  }
  .front-lockup__text {
    font-family: "Barlow Semi Condensed", sans-serif;
    font-weight: 300;
    font-size: 64px;
    line-height: 1;
    letter-spacing: 1px;
  }

  /* Back side */
  .card--back {
    background: var(--paper);
    color: var(--ink);
    display: flex;
    flex-direction: column;
    align-items: center;
    padding-top: 70px;
    text-align: center;
  }
  .brand__dot {
    width: 150px;
    height: 150px;
    border-radius: 50%;
    border: 8px solid var(--ink);
  }
  .brand__name {
    margin-top: 26px;
    font-family: "Barlow Semi Condensed", sans-serif;
    font-weight: 500;
    font-size: 44px;
    letter-spacing: 1px;
    line-height: 1;
  }
  .brand__services {
    margin-top: 10px;
    font-family: "Barlow Semi Condensed", sans-serif;
    font-weight: 500;
    font-size: 17px;
    line-height: 1.25;
    letter-spacing: 0.6px;
    text-transform: uppercase;
  }
  .person {
    margin-top: 48px;
    font-family: "Barlow Semi Condensed", sans-serif;
    font-weight: 600;
    font-size: 24px;
    letter-spacing: 0.5px;
    padding-bottom: 8px;
    border-bottom: 3px solid var(--ink);
  }
  .contact {
    margin-top: 26px;
    font-family: "Open Sans", sans-serif;
    font-size: 17px;
    line-height: 1.4;
    list-style: none;
  }
  .social {
    margin-top: 22px;
    font-family: "Open Sans", sans-serif;
    font-size: 17px;
    line-height: 1.5;
    list-style: none;
    text-align: left;
  }
  .social li { display: flex; align-items: center; gap: 10px; }
  .social__mark {
    width: 12px;
    height: 12px;
    background: var(--ink);
    flex: none;
  }
</style>
</head>
<body>
  <main class="sheet">
    <section class="card card--front" aria-label="Vorderseite">
      <div class="front-lockup">
        <span class="front-lockup__dot" aria-hidden="true"></span>
        <span class="front-lockup__text">ANKER gefällig?</span>
      </div>
    </section>

    <section class="card card--back" aria-label="Rückseite">
      <span class="brand__dot" aria-hidden="true"></span>
      <h1 class="brand__name">LICHTUNG PRAXIS</h1>
      <p class="brand__services">Systemisches Elterncoaching<br>Einzel-, Paar- und Familientherapie</p>
      <p class="person">MIRIAM BRENDEL, M.A.</p>
      <ul class="contact">
        <li>www.lichtung-praxis.net</li>
        <li>miriam@lichtung-praxis.net</li>
        <li>+49 176 0000 4812</li>
      </ul>
      <ul class="social">
        <li><span class="social__mark" aria-hidden="true"></span>lichtungpraxis</li>
        <li><span class="social__mark" aria-hidden="true"></span>lichtungpraxis</li>
      </ul>
    </section>
  </main>
</body>
</html>
```